High End Craft Beer needs a label design update

We would like to update the design of our line of craft beer, named Louis-Benoît. The brand name needs to stay predominant in the design. We initially launched with 2 flavours, but with the addition of the third product, we feel there is not enough differentiation between each flavour, and customers are confused in which flavour they are buying (BELGIAN WHITE, INDIA PALE ALE, and AMBER ALE are the current flavours).

We plan to launch a BLONDE LAGER product, but need the 4 products to be more differentiated between each other.

We are looking for the design of the 3 current products (and also the BLOND LAGER if possible) that would be more differentiated.
Updates

Reason: Hello, I am still looking for options, so I am extending the dead-line by 5 days. Thanks

Target Market(s)

Males (75%), 21 to 40.

Font styles to use
Serif
Sans Serif

Requirements
Must have
• All 4 labels need to be coherent between themselves, but more differentiated than the current design
Should not have
• We don't want to completely "re-brand" the product, as customers currently really like the products and its design. And current customers need to easily "recognize" the product they like at store level. The only problem is the confusion between the flavours.

```html
<!DOCTYPE html>
<html lang="fr">
<head>
<meta charset="utf-8">
<title>Louis-Benoît — Amber Ale Ambrée</title>
<link rel="stylesheet" href="https://fonts.googleapis.com/css2?family=Fira+Sans:wght@300;400;600;700&family=Zilla+Slab:wght@700&display=swap">
<style>
  :root {
    --amber: #b36f12;
    --ink: #3a3a3c;
    --ink-soft: #5a5a5c;
    --paper: #ffffff;
    --ornament-light: #ebe9e6;
    --ornament-dark: #d6d3cf;
  }
  html, body {
    margin: 0;
    padding: 0;
    width: 1153px;
    height: 1200px;
    overflow: hidden;
    background: var(--paper);
  }
  .label {
    display: block;
    width: 1153px;
    height: 1200px;
  }
  .shield-frame { fill: var(--amber); }
  .shield-field { fill: var(--paper); }
  .flavour-band { fill: var(--amber); }
  .ornament-area { fill: url(#ornament-tone); }
  .fleur-mark { fill: var(--amber); }
  .fleur-mark--grey { fill: var(--ink-soft); }
  .brewery-arc {
    font-family: "Fira Sans", sans-serif;
    font-weight: 400;
    font-size: 17px;
    letter-spacing: 2.5px;
    fill: var(--ink);
  }
  .brand-name {
    font-family: "Zilla Slab", serif;
    font-weight: 700;
    fill: var(--amber);
  }
  .origin-line {
    font-family: "Fira Sans", sans-serif;
    font-weight: 300;
    font-size: 25px;
    fill: var(--ink);
  }
  .flavour-name {
    font-family: "Fira Sans", sans-serif;
    font-weight: 700;
    font-size: 40px;
    fill: var(--paper);
  }
  .spec {
    font-family: "Fira Sans", sans-serif;
    font-weight: 300;
    fill: var(--ink);
  }
  .spec--type { font-size: 29px; }
  .spec--volume { font-size: 42px; }
  .spec--abv { font-size: 23px; }
  .rule { stroke: var(--ink); stroke-width: 1.5; fill: none; }
  .rule-end { fill: var(--ink); }
</style>
</head>
<body>
<svg class="label" viewBox="0 0 1153 1200" xmlns="http://www.w3.org/2000/svg">
  <defs>
    <linearGradient id="ornament-tone" x1="0" y1="0" x2="0" y2="1">
      <stop offset="0" stop-color="var(--ornament-dark)"/>
      <stop offset="1" stop-color="var(--ornament-light)"/>
    </linearGradient>
  </defs>

  <!-- Shield -->
  <path class="shield-frame" d="M165,165 H975 V912 C900,960 760,1020 680,1040 Q600,1060 575,1122 Q550,1060 470,1040 C390,1020 250,960 165,912 Z"/>
  <path class="shield-field" d="M187,187 H953 V898 C880,945 750,1003 672,1020 Q596,1040 575,1090 Q554,1040 478,1020 C400,1003 270,945 187,898 Z"/>

  <!-- Crest ornament area -->
  <rect class="ornament-area" role="img" aria-label="Ornamental filigree crest above the brand name"
        x="390" y="212" width="362" height="236" rx="24"/>

  <!-- Brewery name on arc -->
  <path id="brewery-curve" d="M438,518 Q572,452 708,518" fill="none"/>
  <text class="brewery-arc" text-anchor="middle">
    <textPath href="#brewery-curve" startOffset="50%">· BRASSERIE DEUX RIVES ·</textPath>
  </text>
  <rect class="fleur-mark" role="img" aria-label="Small fleur-de-lis ornament" x="544" y="494" width="34" height="34" rx="6"/>

  <!-- Brand name -->
  <text class="brand-name" x="570" y="610" text-anchor="middle" font-size="92" textLength="505" lengthAdjust="spacingAndGlyphs">LOUIS</text>
  <text class="brand-name" x="570" y="720" text-anchor="middle" font-size="120" textLength="505" lengthAdjust="spacingAndGlyphs">BENOÎT</text>

  <!-- Origin line -->
  <rect class="fleur-mark--grey" role="img" aria-label="Small fleur-de-lis ornament" x="332" y="746" width="26" height="28" rx="5"/>
  <text class="origin-line" x="572" y="771" text-anchor="middle" textLength="364" lengthAdjust="spacing">BRASSÉE AU QUÉBEC</text>
  <rect class="fleur-mark--grey" role="img" aria-label="Small fleur-de-lis ornament" x="782" y="746" width="26" height="28" rx="5"/>

  <!-- Flavour band -->
  <rect class="flavour-band" x="165" y="783" width="810" height="56"/>
  <text class="flavour-name" x="571" y="827" text-anchor="middle" textLength="507" lengthAdjust="spacing">AMBER ALE AMBRÉE</text>

  <!-- Specs -->
  <text class="spec spec--type" x="557" y="873" text-anchor="end" textLength="187" lengthAdjust="spacingAndGlyphs">BIÉRE FORTE</text>
  <text class="spec spec--type" x="557" y="913" text-anchor="end" textLength="209" lengthAdjust="spacingAndGlyphs">STRONG BEER</text>
  <line class="rule" x1="569" y1="850" x2="569" y2="912"/>
  <text class="spec spec--volume" x="580" y="885" textLength="158" lengthAdjust="spacingAndGlyphs">500 ML</text>
  <text class="spec spec--abv" x="580" y="913" textLength="175" lengthAdjust="spacingAndGlyphs">6.2 % ALC/VOL</text>

  <!-- Divider rule -->
  <line class="rule" x1="336" y1="930" x2="806" y2="930"/>
  <circle class="rule-end" cx="334" cy="930" r="3.5"/>
  <circle class="rule-end" cx="808" cy="930" r="3.5"/>

  <!-- Lower ornament area -->
  <rect class="ornament-area" role="img" aria-label="Ornamental filigree flourish below the specifications"
        x="505" y="942" width="130" height="76" rx="16"/>
</svg>
</body>
</html>
```